Hi-Tech looking WordPress design for Bright Lane Technologies

We are looking for a creative WordPress design for our client Bright Lane who is a Valtreno copier and printer managed services distributer. They also provide managed IT services.

Target Market(s)

Businesses with 10+ employees

Industry/Entity Type

Printer

Number of Pages Required

1 page

Font styles to use
Sans Serif

Requirements
Must have
• My client distributes and manages Valtreno printers and copy machines to many business industries. They also manage IT network services so their site needs to be hi-tech looking. Their corporate color is Pantone 354C and I've attached their logo.
Nice to have
• A user friendly interface with a top level menu and sliders that will market their services.
Should not have
• Do NOT display the Valtreno logo in their design.

```html
<!DOCTYPE html>
<html lang="en">
<head>
<meta charset="utf-8">
<title>Bright Lane Technologies</title>
<link rel="stylesheet" href="https://fonts.googleapis.com/css2?family=Open+Sans:wght@400;600;700&family=Raleway:wght@500;600;700&display=swap">
<style>
:root{
  --green:#1fa64b;
  --green-dark:#178a3c;
  --ink:#2b2b2b;
  --body:#555;
  --light:#f2f2f2;
  --line:#e2e2e2;
  --footer:#404040;
  --footer-text:#d6d6d6;
  --white:#fff;
}
*{box-sizing:border-box;margin:0;padding:0}
html,body{width:1200px;height:2535px;overflow:hidden}
body{font-family:"Open Sans",Arial,sans-serif;color:var(--body);background:var(--white);font-size:12px}
.wrap{width:876px;margin:0 auto;position:relative}
h2,h3,h4{font-family:"Raleway",Arial,sans-serif;color:var(--ink)}

/* header */
.site-header{height:90px}
.site-header .wrap{height:90px;display:flex;align-items:center;justify-content:space-between}
.brand{display:flex;align-items:center;gap:10px;font-family:"Open Sans",sans-serif;font-size:30px;font-weight:400;color:var(--green)}
.brand-dot{width:40px;height:40px;border-radius:50%;background:var(--green)}
.call{display:flex;align-items:center;gap:10px;color:var(--green);font-weight:700;font-size:13px}
.call-icon{width:24px;height:24px;border-radius:50%;background:var(--green);display:flex;align-items:center;justify-content:center}

.main-nav{height:51px;background:var(--green)}
.main-nav ul{list-style:none;display:flex;height:51px}
.main-nav li{display:flex;align-items:center;padding:0 17px;color:var(--white);font-size:11.5px;font-weight:600;text-transform:uppercase}
.main-nav li.active{background:#3b3b3b;padding:0 24px}

/* hero */
.hero{height:489px;position:relative;overflow:hidden}
.hero-photo{position:absolute;inset:0;background:linear-gradient(100deg,#c9c9c6 0%,#b9b7b3 40%,#8b7f76 65%,#6f6a69 85%,#8a8c90 100%)}
.hero-copy{position:absolute;left:162px;top:136px;color:var(--white)}
.hero-copy h1{font-family:"Raleway",sans-serif;font-weight:700;font-size:26px;line-height:38px;text-transform:uppercase}
.hero-copy p{font-size:16px;line-height:28px;margin-top:14px;width:410px}
.btn{display:inline-flex;align-items:center;gap:6px;background:var(--green);color:var(--white);font-size:11px;font-weight:700;text-transform:uppercase;padding:0 14px;height:40px;border-radius:2px}
.hero .btn{margin-top:26px;height:42px}
.slide-arrow{position:absolute;top:230px;width:32px;height:32px;border-radius:50%;border:1px solid rgba(255,255,255,.6);display:flex;align-items:center;justify-content:center}
.slide-arrow.prev{left:40px}.slide-arrow.next{right:40px}

/* services */
.services{height:437px;background:var(--light);padding-top:37px}
.section-title{text-align:center;font-size:22px;font-weight:600;text-transform:uppercase}
.intro{text-align:center;font-size:11px;line-height:18px;margin-top:22px}
.intro em{color:var(--green)}
.service-grid{display:flex;justify-content:space-between;margin-top:32px}
.service-card{width:277px;height:180px;background:var(--white);border:1px solid var(--line);position:relative;margin-top:52px;text-align:center;padding-top:74px}
.service-icon{position:absolute;left:50%;top:-54px;margin-left:-54px;width:108px;height:108px;border-radius:50%;background:var(--white);border:5px solid var(--green);display:flex;align-items:center;justify-content:center}
.service-icon span{width:84px;height:84px;border-radius:50%;background:var(--green);display:flex;align-items:center;justify-content:center}
.service-card h3{font-size:15px;font-weight:500;text-transform:uppercase}
.service-card p{font-size:11px;line-height:20px;margin:14px auto 0;width:220px}

/* products */
.products{height:445px;padding-top:42px}
.product-grid{display:flex;justify-content:space-between;margin-top:34px}
.product-card{width:206px;height:281px;border:1px solid var(--line);background:#f4f4f4;text-align:center}
.product-photo{height:143px;background:var(--white);display:flex;align-items:center;justify-content:center}
.product-photo div{width:120px;height:118px;border-radius:6px}
.product-card h3{font-family:"Open Sans",sans-serif;font-size:14px;font-weight:400;margin-top:22px}
.product-card p{font-size:10.5px;line-height:18px;margin:10px auto 0;width:170px}
.product-card .model{color:var(--green);font-weight:700;font-size:14px;margin-top:8px}

/* features */
.features{height:371px;background:var(--green);padding-top:42px;color:var(--white)}
.features .section-title{color:var(--white)}
.feature-grid{display:flex;justify-content:space-between;margin-top:30px}
.feature{width:210px;text-align:center}
.feature-icon{width:90px;height:90px;border-radius:50%;border:4px solid var(--white);margin:0 auto;display:flex;align-items:center;justify-content:center}
.feature h3{font-family:"Open Sans",sans-serif;color:var(--white);font-size:17px;font-weight:600;margin-top:18px}
.feature p{font-size:10.5px;line-height:19px;margin-top:10px}

/* why */
.why{height:335px;padding-top:52px}
.why .wrap{display:flex;gap:26px}
.why-photo{width:345px;height:225px;border:3px solid var(--line);background:linear-gradient(120deg,#c9ccd0,#8d8f93 45%,#d7d2cc 70%,#a9aaad)}
.why-text{flex:1}
.why-text h2{font-size:22px;font-weight:600;text-transform:uppercase}
.why-text h2 span{color:var(--green)}
.why-text h4{color:var(--green);font-size:18px;font-weight:600;margin-top:10px}
.why-text p{font-size:10.5px;line-height:21px;margin:12px 0 16px}

/* footer */
.site-footer{height:317px;background:var(--footer);color:var(--footer-text);padding-top:42px}
.footer-cols{display:flex;height:184px}
.footer-col h4{color:var(--white);font-family:"Open Sans",sans-serif;font-size:15px;font-weight:600;text-transform:uppercase;margin-bottom:18px}
.footer-col ul{list-style:none}
.footer-col li{font-size:11px;line-height:20px}
.col-links{width:160px}.col-products{width:187px}.col-contact{width:228px}.col-news{flex:1}
.contact li{display:flex;gap:10px;align-items:flex-start;margin-bottom:6px}
.c-icon{flex:0 0 18px;height:18px;border-radius:50%;border:1px solid var(--footer-text);display:flex;align-items:center;justify-content:center}
.col-news p{font-size:11px;line-height:20px}
.subscribe{display:flex;margin-top:14px;height:40px;border:1px solid #888}
.subscribe span{flex:1;display:flex;align-items:center;padding-left:10px;font-size:11px;color:var(--white)}
.subscribe b{width:105px;background:var(--green);color:var(--white);display:flex;align-items:center;justify-content:center;font-size:13px}
.footer-bottom{border-top:1px solid #5a5a5a;height:49px;display:flex;align-items:center;justify-content:space-between;padding-top:12px}
.footer-brand{display:flex;align-items:center;gap:14px}
.footer-brand .brand{color:var(--white);font-size:26px}
.footer-brand .brand-dot{background:var(--white);width:34px;height:34px}
.footer-brand small{font-size:11px}
.socials{display:flex;gap:6px}
.socials i{width:30px;height:30px;border-radius:50%;border:2px solid var(--white);background:#5a5a5a;display:block}
</style>
</head>
<body>

<header class="site-header">
  <div class="wrap">
    <div class="brand"><span class="brand-dot"></span>Bright Lane</div>
    <div class="call">
      <span class="call-icon"><svg width="12" height="12" viewBox="0 0 24 24"><path fill="#fff" d="M6.6 10.8a15 15 0 0 0 6.6 6.6l2.2-2.2c.3-.3.7-.4 1-.2 1.1.4 2.3.6 3.6.6.6 0 1 .4 1 1V20c0 .6-.4 1-1 1A17 17 0 0 1 3 4c0-.6.4-1 1-1h3.5c.6 0 1 .4 1 1 0 1.3.2 2.5.6 3.6.1.3 0 .7-.2 1z"/></svg></span>
      CALL US: 555-014-2290
    </div>
  </div>
</header>

<nav class="main-nav">
  <ul class="wrap">
    <li class="active">Home</li><li>Why Us</li><li>Products &amp; Services</li><li>Testimonials</li><li>Green</li><li>News</li><li>Helping Hands</li><li>Contact Us</li>
  </ul>
</nav>

<section class="hero">
  <div class="hero-photo" role="img" aria-label="Photo of a hand in a business suit touching a glowing power button"></div>
  <div class="slide-arrow prev"><svg width="10" height="14"><path d="M8 1 2 7l6 6" stroke="#fff" fill="none" stroke-width="1.5"/></svg></div>
  <div class="slide-arrow next"><svg width="10" height="14"><path d="m2 1 6 6-6 6" stroke="#fff" fill="none" stroke-width="1.5"/></svg></div>
  <div class="hero-copy">
    <h1>Power up your business.<br>Think Bright Lane.</h1>
    <p>Sed ut perspiciatis unde omnis iste natussit volup tatem accusa ntium doloremque laudantium</p>
    <span class="btn">Read more <svg width="10" height="10"><circle cx="5" cy="5" r="5" fill="#fff"/><path d="m4 3 2 2-2 2" stroke="#1fa64b" fill="none" stroke-width="1.4"/></svg></span>
  </div>
</section>

<section class="services">
  <div class="wrap">
    <h2 class="section-title">Our Services</h2>
    <p class="intro">Sed ut perspiciatis unde o<em>mnis iste natus error sit voluptatem accusantium doloremqu</em>e lau dantium, totam rem aperiam, eaque ipsa quae ab illo inventore<br>veritatis et quasi architecto beatae vitae dicta sunt explicabomo enim ipsam voluptateSed ut perspiciatis unde omnis iste natus error sit volu</p>
    <div class="service-grid">
      <div class="service-card">
        <div class="service-icon"><span><svg width="40" height="40" viewBox="0 0 40 40"><rect x="11" y="5" width="18" height="10" fill="#fff"/><rect x="4" y="15" width="32" height="14" rx="2" fill="#fff"/><rect x="11" y="24" width="18" height="12" fill="#fff" stroke="#1fa64b" stroke-width="2"/></svg></span></div>
        <h3>Valtreno Printers</h3>
        <p>Sed ut perspiciatis unde omnis iste natus error sit voluptatem accusantiumolo.</p>
      </div>
      <div class="service-card">
        <div class="service-icon"><span><svg width="40" height="40" viewBox="0 0 40 40"><rect x="10" y="4" width="20" height="8" fill="#fff"/><rect x="8" y="13" width="24" height="23" fill="#fff"/><path d="M12 20h16M12 26h16M12 31h16" stroke="#1fa64b" stroke-width="2"/></svg></span></div>
        <h3>Copy Machines</h3>
        <p>Sed ut perspiciatis unde omnis iste natus error sit voluptatem accusantiumolo.</p>
      </div>
      <div class="service-card">
        <div class="service-icon"><span><svg width="42" height="42" viewBox="0 0 40 40"><circle cx="20" cy="20" r="16" fill="#fff"/><path d="M9 13c5 1 7 5 5 9s2 7 0 10M22 5c-2 5 3 6 6 8s1 7 5 8M20 36c1-5 6-5 8-9" stroke="#1fa64b" stroke-width="3" fill="none"/></svg></span></div>
        <h3>IT Network Services</h3>
        <p>Sed ut perspiciatis unde omnis iste natus error sit voluptatem accusantiumolo.</p>
      </div>
    </div>
  </div>
</section>

<section class="products">
  <div class="wrap">
    <h2 class="section-title">Our Products</h2>
    <div class="product-grid">
      <div class="product-card">
        <div class="product-photo"><div role="img" aria-label="Photo of a black multifunction office copier" style="background:linear-gradient(#4a4a4a,#1e1e1e)"></div></div>
        <h3>Used Equipment</h3>
        <p>Sed ut perspiciatis unde os isns error loresitatem acculntlo.</p>
        <div class="model">VT-310e</div>
      </div>
      <div class="product-card">
        <div class="product-photo"><div role="img" aria-label="Photo of a white desktop colour laser printer" style="background:linear-gradient(#eeeeee,#b9b9b9)"></div></div>
        <h3>Printers, Color</h3>
        <p>Sed ut perspiciatis unde os isns error loresitatem acculntlo.</p>
        <div class="model">LUMA C2140DN</div>
      </div>
      <div class="product-card">
        <div class="product-photo"><div role="img" aria-label="Photo of a beige fax machine" style="background:linear-gradient(#efe6d8,#c7b9a4)"></div></div>
        <h3>Fax Machines</h3>
        <p>Sed ut perspiciatis unde os isns error loresitatem acculntlo.</p>
        <div class="model">VT-310e</div>
      </div>
      <div class="product-card">
        <div class="product-photo"><div role="img" aria-label="Photo of a large white black and white office printer" style="background:linear-gradient(#f2f2f2,#a8a8a8)"></div></div>
        <h3>Printers, Black &amp; White</h3>
        <p>Sed ut perspiciatis unde os isns error loresitatem acculntlo.</p>
        <div class="model">VT-310e</div>
      </div>
    </div>
  </div>
</section>

<section class="features">
  <div class="wrap">
    <h2 class="section-title">Our Features</h2>
    <div class="feature-grid">
      <div class="feature">
        <div class="feature-icon"><svg width="44" height="40" viewBox="0 0 44 40"><rect x="3" y="8" width="38" height="12" rx="2" fill="#fff"/><rect x="9" y="20" width="26" height="10" fill="#fff"/><path d="M12 30v8M32 30v8" stroke="#fff" stroke-width="3"/></svg></div>
        <h3>Printing</h3>
        <p>At vero eos et accusamus eodioig nissimqui blan lodit iisaestiu volup tatum deleniti atqloreucorru.</p>
      </div>
      <div class="feature">
        <div class="feature-icon"><svg width="44" height="40" viewBox="0 0 44 40"><path d="M4 28 30 6l5 5-22 23z" fill="none" stroke="#fff" stroke-width="3"/><rect x="4" y="28" width="36" height="8" rx="2" fill="#fff"/></svg></div>
        <h3>Scanning</h3>
        <p>At vero eos et accusamus eodioig nissimqui blan lodit iisaestiu volup tatum deleniti atqloreucorru.</p>
      </div>
      <div class="feature">
        <div class="feature-icon"><svg width="40" height="40" viewBox="0 0 40 40"><rect x="4" y="12" width="8" height="24" rx="2" fill="#fff"/><rect x="14" y="4" width="20" height="10" fill="none" stroke="#fff" stroke-width="2"/><rect x="14" y="16" width="22" height="20" rx="2" fill="#fff"/><path d="M18 22h4M26 22h4M18 28h4M26 28h4" stroke="#1fa64b" stroke-width="2.5"/></svg></div>
        <h3>Faxing</h3>
        <p>At vero eos et accusamus eodioig nissimqui blan lodit iisaestiu volup tatum deleniti atqloreucorru.</p>
      </div>
      <div class="feature">
        <div class="feature-icon"><svg width="40" height="40" viewBox="0 0 40 40"><rect x="8" y="4" width="24" height="7" fill="#fff"/><rect x="6" y="12" width="28" height="24" fill="#fff"/><path d="M10 19h20M10 25h20M10 31h20" stroke="#1fa64b" stroke-width="2"/></svg></div>
        <h3>Copier Memory</h3>
        <p>At vero eos et accusamus eodioig nissimqui blan lodit iisaestiu volup tatum deleniti atqloreucorru.</p>
      </div>
    </div>
  </div>
</section>

<section class="why">
  <div class="wrap">
    <div class="why-photo" role="img" aria-label="Photo of two office colleagues unpacking a new copier"></div>
    <div class="why-text">
      <h2>Why choosing an <span>office copier</span></h2>
      <h4>What is my volume?</h4>
      <p>Once you decide on the features you need, the next step is to narrow your choices based on the number of copies/prints you make in a month. You can use your monthly paper consumption to help determine your current copy/print volume. Once you have a rough volume figure and you have decided to have the print feature, increase the figure by 30% to accommodate your new needs.</p>
      <span class="btn">Read more <svg width="10" height="10"><circle cx="5" cy="5" r="5" fill="#fff"/><path d="m4 3 2 2-2 2" stroke="#1fa64b" fill="none" stroke-width="1.4"/></svg></span>
    </div>
  </div>
</section>

<footer class="site-footer">
  <div class="wrap">
    <div class="footer-cols">
      <div class="footer-col col-links">
        <h4>Links</h4>
        <ul><li>About</li><li>Our Services</li><li>Our Products</li><li>Why Choose Us</li><li>Locations</li><li>Blog</li></ul>
      </div>
      <div class="footer-col col-products">
        <h4>Products</h4>
        <ul><li>Used Equipment</li><li>Copiers, Color</li><li>Printers, Black &amp; White</li><li>Fax Machines</li><li>Copiers, Black &amp; White</li><li>Document Management</li></ul>
      </div>
      <div class="footer-col col-contact">
        <h4>Contact Us</h4>
        <ul class="contact">
          <li><span class="c-icon"><svg width="8" height="10" viewBox="0 0 8 10"><path d="M4 10S0 6 0 4a4 4 0 0 1 8 0c0 2-4 6-4 6z" fill="#d6d6d6"/></svg></span>Postal address: PO Box 218,<br>Elmstead sample street lor</li>
          <li><span class="c-icon"><svg width="8" height="8" viewBox="0 0 24 24"><path fill="#d6d6d6" d="M6.6 10.8a15 15 0 0 0 6.6 6.6l2.2-2.2c.3-.3.7-.4 1-.2 1.1.4 2.3.6 3.6.6.6 0 1 .4 1 1V20c0 .6-.4 1-1 1A17 17 0 0 1 3 4c0-.6.4-1 1-1h3.5c.6 0 1 .4 1 1 0 1.3.2 2.5.6 3.6.1.3 0 .7-.2 1z"/></svg></span>Phone: 555-014-2290</li>
          <li><span class="c-icon"><svg width="9" height="8" viewBox="0 0 9 8"><rect x="0" y="2" width="9" height="6" fill="#d6d6d6"/><rect x="2" y="0" width="5" height="2" fill="#d6d6d6"/></svg></span>Fax: 555-014-7731</li>
          <li><span class="c-icon"><svg width="9" height="7" viewBox="0 0 9 7"><rect width="9" height="7" fill="#d6d6d6"/><path d="m0 0 4.5 4L9 0" stroke="#404040" fill="none"/></svg></span>hello@brightlane.example</li>
        </ul>
      </div>
      <div class="footer-col col-news">
        <h4>Newsletter</h4>
        <p>Sed ut perspiciatis unde omnis iste natus error sit voluptatem usantium doloremque laudantium, totam rem aperiameu</p>
        <div class="subscribe"><span>Email address</span><b>SUBSCRIBE</b></div>
      </div>
    </div>
    <div class="footer-bottom">
      <div class="footer-brand">
        <div class="brand"><span class="brand-dot"></span>Bright Lane</div>
        <small>© 2016 Think Bright Lane | Privacy | Terms &amp; Conditions</small>
      </div>
      <div class="socials"><i></i><i></i><i></i><i></i></div>
    </div>
  </div>
</footer>

</body>
</html>
```